Need a book cover design for a Lumora Book

Book has a long title and sub title so lots of words to fit on the cover.

I can be flexible a bit with the sub title due to the length of it but ideally i can get a design that takes everything.

Here is the title:

Tidal Geology: The Roots of Erosion, Sedimentation, and Canyon Forming

Sub Title/Heading
An Easy Primer on Coastal Cliffs, Dune Drift, River Beds, and Delta Mapping Methods

```html
<!DOCTYPE html>
<html lang="en">
<head>
<meta charset="utf-8">
<title>Tidal Geology — Book Cover</title>
<link rel="stylesheet" href="https://fonts.googleapis.com/css2?family=Noto+Sans:wght@400&display=swap">
<style>
  :root {
    --ink-dark: #0a0e11;
    --teal: #4fb3c4;
    --teal-mid: #2d7f8e;
    --teal-deep: #1b4f5a;
    --amber: #c08450;
    --amber-deep: #7a5030;
    --panel: rgba(28, 28, 28, 0.5);
    --text: #ffffff;
  }
  html, body {
    margin: 0;
    padding: 0;
    width: 750px;
    height: 1200px;
    overflow: hidden;
    background: var(--ink-dark);
  }
  .cover {
    position: relative;
    width: 750px;
    height: 1200px;
    overflow: hidden;
    font-family: "Noto Sans", "DejaVu Sans", sans-serif;
    color: var(--text);
  }
  .cover-art {
    position: absolute;
    inset: 0;
    background:
      radial-gradient(ellipse 45% 14% at 80% 8%, rgba(79,179,196,0.75), transparent 72%),
      radial-gradient(ellipse 40% 10% at 20% 4%, rgba(45,127,142,0.6), transparent 72%),
      radial-gradient(ellipse 30% 18% at 5% 30%, rgba(45,127,142,0.6), transparent 72%),
      radial-gradient(ellipse 35% 14% at 4% 47%, rgba(192,132,80,0.6), transparent 72%),
      radial-gradient(ellipse 25% 30% at 100% 45%, rgba(45,127,142,0.55), transparent 72%),
      radial-gradient(ellipse 65% 9% at 45% 52%, rgba(45,127,142,0.5), transparent 75%),
      radial-gradient(ellipse 70% 12% at 35% 58%, rgba(79,179,196,0.55), transparent 75%),
      radial-gradient(ellipse 55% 10% at 35% 66%, rgba(192,132,80,0.4), transparent 75%),
      radial-gradient(ellipse 35% 14% at 10% 72%, rgba(79,179,196,0.55), transparent 72%),
      radial-gradient(ellipse 30% 20% at 92% 72%, rgba(192,132,80,0.5), transparent 72%),
      radial-gradient(ellipse 25% 14% at 5% 84%, rgba(192,132,80,0.55), transparent 72%),
      radial-gradient(ellipse 30% 25% at 95% 92%, rgba(192,132,80,0.6), transparent 72%),
      radial-gradient(ellipse 50% 10% at 35% 92%, rgba(79,179,196,0.6), transparent 72%),
      radial-gradient(ellipse 40% 8% at 60% 98%, rgba(45,127,142,0.55), transparent 72%),
      linear-gradient(160deg, #0e181c 0%, var(--ink-dark) 45%, #0f171a 100%);
  }
  .title-panel {
    position: absolute;
    left: 79px;
    top: 199px;
    width: 592px;
    height: 848px;
    background: var(--panel);
  }
  .book-title {
    position: absolute;
    left: 100px;
    top: 268px;
    width: 570px;
    margin: 0;
    font-weight: 400;
  }
  .title-main {
    display: block;
    font-size: 54px;
    line-height: 64px;
    letter-spacing: 0.5px;
  }
  .title-sub {
    display: block;
    font-size: 32px;
    line-height: 58px;
    margin-top: -4px;
  }
  .book-subtitle {
    position: absolute;
    left: 105px;
    top: 822px;
    width: 555px;
    margin: 0;
    font-size: 36px;
    line-height: 47px;
    font-weight: 400;
  }
</style>
</head>
<body>
  <main class="cover">
    <div class="cover-art" role="img" aria-label="Abstract flowing strands of teal and amber light weaving across a dark background"></div>
    <div class="title-panel"></div>
    <h1 class="book-title">
      <span class="title-main">Tidal Geology:</span>
      <span class="title-sub">The Roots of Erosion, Sedimentation, and Canyon Forming</span>
    </h1>
    <p class="book-subtitle">An Easy Primer on Coastal Cliffs, Dune Drift, River Beds, and Delta Mapping Methods</p>
  </main>
</body>
</html>
```